Lotus Bowl take out menu

We need a take out menu design using our menu attached. Info to include would be our address: 5817 Meridel Harrow Pkwy #204, Lafayette, LA 70508. Phone number is 337-614-2953. website is www.lotusbowlvtr.example.

Industry/Entity Type

Asian Restaurant

```html
<!DOCTYPE html>
<html lang="en">
<head>
<meta charset="utf-8">
<title>Lotus Bowl — Take out menu</title>
<link rel="stylesheet" href="https://fonts.googleapis.com/css2?family=Kite+One&display=swap">
<style>
  :root {
    --paper: #f5eded;
    --paper-deep: #eddcdc;
    --maroon: #7a1a1e;
    --ink: #2a1a1a;
    --rule: #c9a7a7;
    --chili: #d8232a;
  }
  * { margin: 0; padding: 0; box-sizing: border-box; }
  html, body { width: 1200px; height: 853px; overflow: hidden; }
  body {
    position: relative;
    background: var(--paper);
    font-family: "Kite One", sans-serif;
    color: var(--ink);
  }
  .backdrop {
    position: absolute; inset: 0;
    background: radial-gradient(ellipse at 50% 50%, #f8f1f1 0%, var(--paper) 55%, var(--paper-deep) 100%);
  }
  .top-rule { position: absolute; left: 0; top: 28px; width: 1200px; height: 2px; background: var(--maroon); }
  .column-rule { position: absolute; top: 40px; width: 1px; height: 780px; background: var(--rule); }
  .section-title {
    position: absolute; font-size: 14px; font-weight: 400; letter-spacing: 1.8px;
    color: var(--maroon); text-transform: uppercase; transform: translateX(-50%); white-space: nowrap;
  }
  .menu-item { position: absolute; left: 29px; width: 360px; }
  .menu-item .name { font-size: 9.5px; color: var(--maroon); letter-spacing: 1px; line-height: 11px; }
  .menu-item .desc { font-size: 9px; letter-spacing: 1px; line-height: 10.8px; width: 322px; }
  .menu-item .price { position: absolute; left: 338px; top: 2px; font-size: 8.8px; }
  .item-rule { position: absolute; left: 29px; width: 356px; height: 1px; background: var(--rule); }
  .chili { display: inline-block; vertical-align: -1px; margin-left: 4px; }
  .story {
    position: absolute; left: 424px; top: 86px; width: 350px;
    font-size: 10.6px; line-height: 14.3px; letter-spacing: 1px; text-align: justify;
  }
  .badge {
    position: absolute; left: 479px; top: 422px; width: 226px; height: 214px;
    display: flex; align-items: center; justify-content: center;
  }
  .badge .brand { font-size: 28px; color: var(--maroon); letter-spacing: 1px; }
  .contact { position: absolute; left: 410px; width: 380px; text-align: center; font-size: 11.6px; letter-spacing: 1px; white-space: nowrap; }
  .contact svg { vertical-align: -2px; margin-right: 6px; }
  .brand-block { position: absolute; left: 830px; top: 140px; width: 320px; text-align: center; }
  .brand-block .brand { font-size: 46px; color: var(--ink); line-height: 50px; }
  .brand-block .tagline { font-size: 12px; letter-spacing: 2.4px; color: var(--ink); margin-top: 2px; }
  .panel-rule { position: absolute; left: 808px; width: 372px; height: 1px; background: var(--rule); }
  .takeout { position: absolute; left: 808px; top: 328px; width: 372px; text-align: center; font-size: 18px; letter-spacing: 1.4px; }
  .art {
    position: absolute; left: 824px; top: 428px; width: 342px; height: 366px;
    background: linear-gradient(135deg, rgba(122,26,30,.08), rgba(216,35,42,.18));
    border-radius: 4px;
  }
</style>
</head>
<body>
  <div class="backdrop" role="img" aria-label="Soft pink wave and dragon line pattern"></div>
  <div class="top-rule"></div>
  <div class="column-rule" style="left:402px"></div>
  <div class="column-rule" style="left:797px"></div>

  <h2 class="section-title" style="left:205px;top:45px">Appetizers</h2>

  <div class="menu-item" style="top:92px"><div class="name">Edamame</div><div class="desc">Seasoned &amp; boiled soy bean</div><div class="price">$16</div></div>
  <div class="item-rule" style="top:122px"></div>
  <div class="menu-item" style="top:128px"><div class="name">Scallion Pancakes</div><div class="desc">Traditional Chinese flatbread folded with oil and minced scallions and pan fried</div><div class="price">$18</div></div>
  <div class="item-rule" style="top:168px"></div>
  <div class="menu-item" style="top:174px"><div class="name">Lotus Bowl Lettuce Wraps</div><div class="desc">Seasoned ground chicken drizzled with our top secret homemade sauce served with lettuce wraps</div><div class="price">$15</div></div>
  <div class="item-rule" style="top:215px"></div>
  <div class="menu-item" style="top:221px"><div class="name">Salt &amp; Pepper Calamari</div><div class="desc">Crispy Calamari with Green &amp; red peppers and onions</div><div class="price">$15</div></div>
  <div class="item-rule" style="top:251px"></div>
  <div class="menu-item" style="top:257px"><div class="name">Buddha Bang Shrimp</div><div class="desc">Crispy fried shrimp tossed in our creamy spicy sauce</div><div class="price">$14</div></div>
  <div class="item-rule" style="top:286px"></div>
  <div class="menu-item" style="top:292px"><div class="name">Drunken Chicken<svg class="chili" width="12" height="9" viewBox="0 0 12 9"><path d="M1 6 Q6 9 11 1 Q8 5 1 6Z" fill="var(--chili)"/></svg></div><div class="desc">Chicken, Thai chili in a house made spicy sauce</div><div class="price">$14</div></div>
  <div class="item-rule" style="top:322px"></div>
  <div class="menu-item" style="top:328px"><div class="name">Sichuan Spiced Beef<svg class="chili" width="24" height="9" viewBox="0 0 24 9"><path d="M1 6 Q6 9 11 1 Q8 5 1 6Z M13 6 Q18 9 23 1 Q20 5 13 6Z" fill="var(--chili)"/></svg></div><div class="desc">Beef Shank, beef tripe, cilantro, peanuts and celery</div><div class="price">$14</div></div>
  <div class="item-rule" style="top:358px"></div>
  <div class="menu-item" style="top:364px"><div class="name">Beef Crispy Bottom Bao</div><div class="desc">Pan fried crispy bottom Bao, stuffed with beef, drizzled with scallion and sesame (Fresh made to order, takes at least 20 mins to serve)</div><div class="price">$14</div></div>
  <div class="item-rule" style="top:415px"></div>
  <div class="menu-item" style="top:421px"><div class="name">Shrimp &amp; Beef Crispy Bottom Bao</div><div class="desc">Pan fried crispy bottom Bao, stuffed with beef and shrimp, drizzled with scallion and sesame (Fresh made to order, takes at least 20 mins to serve)</div><div class="price">$14</div></div>
  <div class="item-rule" style="top:476px"></div>
  <div class="menu-item" style="top:484px"><div class="name">Crispy Mala Beef Jerky<svg class="chili" width="24" height="9" viewBox="0 0 24 9"><path d="M1 6 Q6 9 11 1 Q8 5 1 6Z M13 6 Q18 9 23 1 Q20 5 13 6Z" fill="var(--chili)"/></svg></div><div class="desc">Dry fried shredded beef with various peppers in sesame and peppercorn oil</div><div class="price">$14</div></div>
  <div class="item-rule" style="top:524px"></div>
  <div class="menu-item" style="top:531px"><div class="name">Fried Chicken Dumplings (6)</div><div class="desc">Chinese dumpling stuffed with Chicken, Shiitake mushrooms and bamboo shoots</div><div class="price">$14</div></div>
  <div class="item-rule" style="top:571px"></div>
  <div class="menu-item" style="top:577px"><div class="name">Red Oil Dumplings (6)<svg class="chili" width="12" height="9" viewBox="0 0 12 9"><path d="M1 6 Q6 9 11 1 Q8 5 1 6Z" fill="var(--chili)"/></svg></div><div class="desc">Pork filled dumplings in Sichuan red oil sauce drizzled with sesame</div><div class="price">$14</div></div>
  <div class="item-rule" style="top:617px"></div>
  <div class="menu-item" style="top:623px"><div class="name">Pork Egg Rolls (2)</div><div class="desc">Hand rolled with julienned veggies with our sweet n' sour mustard sauce</div><div class="price">$14</div></div>
  <div class="item-rule" style="top:664px"></div>
  <div class="menu-item" style="top:670px"><div class="name">Vegetarian Spring Rolls (3)</div><div class="desc">Traditional Asian Roll served with a sweet chili sauce</div><div class="price">$14</div></div>
  <div class="item-rule" style="top:700px"></div>
  <div class="menu-item" style="top:706px"><div class="name">Garlic Cucumber Salad</div><div class="desc">Sliced cucumber with a garlic vinaigrette</div><div class="price">$14</div></div>
  <div class="item-rule" style="top:736px"></div>
  <div class="menu-item" style="top:742px"><div class="name">Hot n' Sour Soup<svg class="chili" width="12" height="9" viewBox="0 0 12 9"><path d="M1 6 Q6 9 11 1 Q8 5 1 6Z" fill="var(--chili)"/></svg></div><div class="desc">Tangy broth with Bamboo shoot, wood ear fungus, tofu, egg and carrots</div><div class="price">$14</div></div>
  <div class="item-rule" style="top:782px"></div>
  <div class="menu-item" style="top:788px"><div class="name">West Lake Soup</div><div class="desc">Light creamy soup with ground beef, diced Shiitake mushroom, tofu, bamboo shoots, egg white and cilantro</div><div class="price">$14</div></div>

  <h2 class="section-title" style="left:598px;top:44px">Our Story</h2>
  <p class="story">At Lotus Bowl, we pride ourselves in serving fresh, authentic Sichuan Chinese cuisine delicately prepared by our expertly trained Chefs.<br>
  Sichuan cuisine originates from southwest China between the Sichuan Basin and Tibetan Plateau. It is known for being both very spicy and flavorful, much like our own southern Louisiana cuisine.<br>
  Our Executive Chef, Wen Lo grew up in the southwestern Chinese province of Sichuan, China where he began his training at fifteen years old under his grandfather's mentorship. Chef Lo became an acclaimed chef in his province, opening several restaurants and traveling throughout China to cater for many of China's elite. His dream was to share his Sichuan style with the world which lead him to the United States. He has worked in restaurants in both Houston and New York and we now welcome him to his new home in Lafayette, Louisiana.<br>
  We are very excited to bring to Lafayette the authenticity of Chinese cuisine and hope you enjoy your experience dining with us.</p>

  <div class="badge"><span class="brand">Lotus Bowl</span></div>

  <div class="contact" style="top:714px">
    <svg width="10" height="14" viewBox="0 0 10 14"><path d="M5 0a5 5 0 0 0-5 5c0 4 5 9 5 9s5-5 5-9a5 5 0 0 0-5-5zm0 7a2 2 0 1 1 0-4 2 2 0 0 1 0 4z" fill="var(--maroon)"/></svg>5817 Meridel Harrow Pkwy #204, Lafayette, LA 70508
  </div>
  <div class="contact" style="top:744px">
    <svg width="12" height="12" viewBox="0 0 12 12"><path d="M2.5 0.5l2 2.5-1.2 1.5c.8 1.7 2 2.9 3.7 3.7L8.5 7l2.5 2-1 2.5C5 11.5.5 7 .5 2z" fill="var(--maroon)"/></svg>337-614-2953
  </div>
  <div class="contact" style="top:773px;font-size:10px">
    <svg width="12" height="12" viewBox="0 0 12 12" fill="none" stroke="var(--maroon)" stroke-width="1"><circle cx="6" cy="6" r="5.3"/><ellipse cx="6" cy="6" rx="2.4" ry="5.3"/><path d="M.7 6h10.6M1.5 3.3h9M1.5 8.7h9"/></svg>www.lotusbowlvtr.example
  </div>

  <div class="brand-block">
    <div class="brand">Lotus Bowl</div>
    <div class="tagline">Fresh Asian Cuisine</div>
  </div>
  <div class="panel-rule" style="top:297px"></div>
  <div class="takeout">Take out menu</div>
  <div class="panel-rule" style="top:377px"></div>
  <div class="art" role="img" aria-label="Illustration of a pair of red and black chopsticks holding a red chili pepper"></div>
</body>
</html>
```